I want our new logo design to guide the colors and look of the home page. I want it to be vibrant and contemporary. We are a new religious education publishing company. I would like any colors used to describe the product below to be bright and cheerful, but also to look good with our logo colors
On our home page we are introducing a new product for second graders. The product name should look child friendly, but not silly. If there is a way to add reverence to the words FIRST RECONCILIATION and FIRST EUCHARIST, and still make it look like it is a product for children, that would be great.
The product will be called:
Little Pilgrim Learning Set for the Open Door Room
FIRST RECONCILIATION
FIRST EUCHARIST
THE PRODUCT DESCRIPTION SHOULD BE AS FOLLOWS
Field tested and designed for the special needs inclusive classroom
Kit includes high impact visuals, hands-on activities, manipulatives, games, and other teaching aids for total engagement of ALL students
Detailed catechist lesson plans to maximize learning and retention
Cost effective reusable kit
Bilingual
Somewhere it should say COMING SOON, because the product is not ready yet, but we are promoting it. I don't have a picture of this product yet, but above the product description, we need an empty box that we'll use when we're ready to upload the picture of the kit.
There should also be a statement near the product description that says: To learn more about the Little Pilgrim Set for the Open Door Room, click here.
Web page links:
About Us
Products
Resources
Contact Us
I would also like a few links to be featured on the home page:
Faith Lessons for Tomorrow's Hearts....learn more
"Where Do We Begin?"....learn more
Could It Be Something Deeper Inside?...learn more
The Dream and the Daily...learn more
Genuine Welcoming Formation
I have increased my budget and clarified my brief so that it's easier to understand. It's basically just a home page and a template for the other pages. There is no content on the other web pages that you have to work on. I just need a well designed home page and a nice template for the other pages.
Reason: I am extending the deadline for 2 days so that templates can be designed for 5 additional web pages. Please make each template a little different from the way you designed the home page. These pages can have blank picture boxes and dummy text to save you time. I am only interested in layout for the addtional pages. Thank you!
We've made a selection and wanted to thank all of you for your wonderful designs!

```html
<!DOCTYPE html>
<html lang="en">
<head>
<meta charset="utf-8">
<title>Bright Shore Catechetics</title>
<link rel="stylesheet" href="https://fonts.googleapis.com/css2?family=Arimo:ital,wght@0,400;0,700;1,400&display=swap">
<style>
  :root {
    --bg-red: #b8161b;
    --bg-orange: #e2621a;
    --brand-red: #c0161d;
    --accent-orange: #f39200;
    --hot-orange: #d8431a;
    --tab-light: #d9705a;
    --ink: #1c1c1c;
    --rule: #e2e2e2;
    --box-line: #cfcfcf;
    --card: #ffffff;
  }
  * { box-sizing: border-box; margin: 0; padding: 0; }
  html, body { width: 1200px; height: 887px; overflow: hidden; }
  body {
    font-family: "Arimo", Arial, sans-serif;
    color: var(--ink);
    background: radial-gradient(ellipse 70% 60% at 50% 35%, var(--bg-orange) 0%, #cf3a19 45%, var(--bg-red) 100%);
    position: relative;
  }
  .topbar {
    position: absolute; top: 9px; right: 94px;
    display: flex; align-items: center;
    color: #fff; font-size: 13px;
  }
  .topbar .phone { display: flex; align-items: center; gap: 6px; margin-right: 20px; }
  .social { display: flex; gap: 4px; }
  .social span { width: 16px; height: 16px; border-radius: 2px; display: block; }
  .social .s1 { background: #3b5998; } .social .s2 { background: #33a8d9; }
  .social .s3 { background: #2a6ea8; } .social .s4 { background: #f07d1e; }

  .card {
    position: absolute; left: 78px; top: 35px; width: 1038px; height: 755px;
    background: var(--card); border-radius: 7px; overflow: hidden;
  }
  .header {
    height: 117px; position: relative;
    background: linear-gradient(#fff, #f3f3f3);
    border-bottom: 3px solid var(--brand-red);
  }
  .brand {
    position: absolute; left: 38px; top: 38px;
    display: flex; align-items: center; gap: 10px;
  }
  .brand .dot { width: 26px; height: 26px; border-radius: 50%; background: var(--accent-orange); }
  .brand .name { font-size: 24px; font-weight: 700; color: var(--brand-red); }
  .nav { position: absolute; top: 46px; left: 464px; display: flex; }
  .nav a {
    font-size: 15px; color: #333; text-decoration: none;
    height: 28px; line-height: 28px; border-radius: 6px;
  }
  .nav a.active { color: #fff; padding: 0 16px; background: linear-gradient(#f59a1a, #dc4c16); }
  .nav a:nth-child(2) { margin-left: 43px; }
  .nav a:nth-child(3) { margin-left: 46px; }
  .nav a:nth-child(4) { margin-left: 49px; }
  .nav a:nth-child(5) { margin-left: 45px; }

  .hero { position: relative; height: 346px; }
  .hero-photo {
    position: absolute; inset: 0;
    background: linear-gradient(100deg, #6b6a66 0%, #8f8a80 35%, #b58a6e 55%, #d9b89e 70%, #6e5442 100%);
  }
  .hero-panel {
    position: absolute; left: 0; top: 131px; width: 464px; height: 192px;
    background: rgba(205, 64, 24, 0.85); color: #fff; padding: 22px 28px;
  }
  .hero-panel h1 { font-weight: 400; font-size: 24px; margin-bottom: 17px; }
  .hero-panel p { font-size: 12.5px; line-height: 14.5px; }
  .hero-panel em { color: var(--accent-orange); }
  .dots { position: absolute; left: 28px; bottom: 22px; display: flex; gap: 8px; }
  .dots span { width: 76px; height: 5px; background: rgba(240,140,110,0.75); }
  .dots span.on { background: #fff; }

  .content { display: flex; padding-top: 39px; }
  .col { font-size: 12.5px; line-height: 14.8px; color: #222; }
  .col.one { margin-left: 28px; width: 292px; }
  .col.two { margin-left: 54px; width: 292px; }
  .col.three { margin-left: 44px; width: 302px; }
  .col h2 {
    font-weight: 400; font-size: 20px; line-height: 24px; color: #111;
    padding-bottom: 10px; border-bottom: 1px solid var(--rule); margin-bottom: 11px;
  }
  .col.one h2 { padding-right: 80px; }
  .col h2 span { color: var(--brand-red); }
  .col p { margin-bottom: 10px; }
  .kit-photo {
    float: left; width: 58px; height: 58px; margin: 2px 10px 4px 0;
    border: 1px dashed var(--box-line); background: #fafafa;
  }
  .product-name { display: block; color: var(--brand-red); font-weight: 700; }
  .more { color: var(--brand-red); font-style: italic; clear: both; }
  .links { list-style: none; }
  .links li { margin-bottom: 1px; }
  .links a { color: #222; text-decoration: none; }
  .links a span { color: var(--brand-red); font-style: italic; }

  .news-title { display: flex; align-items: center; gap: 10px; font-size: 20px; margin-bottom: 9px; }
  .news-title .feed { width: 25px; height: 25px; border-radius: 4px; background: #f08a24; }
  .tabs { display: flex; width: 290px; margin-bottom: 12px; }
  .tabs span { flex: 1; text-align: center; color: #fff; font-size: 13px; line-height: 23px; background: var(--tab-light); }
  .tabs span.on { background: var(--hot-orange); }
  .news-item { margin-bottom: 13px; }
  .news-item .headline { display: block; color: #cc2a10; }

  .footer {
    position: absolute; top: 811px; width: 100%; text-align: center;
    color: #fff; font-size: 13px;
  }
  .footer span { color: var(--accent-orange); }
</style>
</head>
<body>
  <div class="topbar">
    <div class="phone">
      <svg width="17" height="11" viewBox="0 0 17 11" aria-hidden="true"><path d="M1 4c0-3 15-3 15 0v2h-4V4H5v2H1z M4 6h9l2 5H2z" fill="#fff"/></svg>
      555-0142-7788
    </div>
    <div class="social"><span class="s1"></span><span class="s2"></span><span class="s3"></span><span class="s4"></span></div>
  </div>

  <div class="card">
    <header class="header">
      <div class="brand"><span class="dot"></span><span class="name">Bright Shore Catechetics</span></div>
      <nav class="nav">
        <a class="active" href="#">Home</a>
        <a href="#">About Us</a>
        <a href="#">Products</a>
        <a href="#">Resources</a>
        <a href="#">Contact Us</a>
      </nav>
    </header>

    <section class="hero">
      <div class="hero-photo" role="img" aria-label="Photo of smiling students in a library"></div>
      <div class="hero-panel">
        <h1>Where Do We Begin?</h1>
        <p>Duis autem vel eum iriure dolor in hendrerit in vulputate velit esse molestie consequat, vel illum dolore eu feugiat nulla facilisis at vero eros et accumsan et iusto odio dignissim qui blandit praesent luptatum zzril delenit augue duis dolore te feugait nulla facilisi. <em>Readmore</em></p>
        <div class="dots"><span></span><span class="on"></span><span></span><span></span></div>
      </div>
    </section>

    <section class="content">
      <div class="col one">
        <h2>Special <span>needs</span> inclusive classroom</h2>
        <div class="kit-photo" role="img" aria-label="Empty box reserved for the kit picture"></div>
        <p><span class="product-name">Little Pilgrim Learning Set for the Open Door Room</span>Kit includes high impact visuals, hands-on activities, manipulatives, games, and other teaching aids for total engagement of all students.</p>
        <p>Detailed catechist lesson plans to maximize learning and retention. Cost effective reusable kit. Bilingual.</p>
        <p class="more">To learn more about the Little Pilgrim Set for the Open Door Room, click here.</p>
      </div>
      <div class="col two">
        <h2>First <span>Reconciliation</span> &amp;<br>First <span>Eucharist</span> Coming Soon...</h2>
        <p>Field tested and designed for the special needs inclusive classroom.</p>
        <ul class="links">
          <li><a href="#">Faith Lessons for Tomorrow's Hearts <span>learn more</span></a></li>
          <li><a href="#">"Where Do We Begin?" <span>learn more</span></a></li>
          <li><a href="#">Could It Be Something Deeper Inside? <span>learn more</span></a></li>
          <li><a href="#">The Dream and the Daily <span>learn more</span></a></li>
          <li><a href="#">Genuine Welcoming Formation <span>learn more</span></a></li>
        </ul>
      </div>
      <div class="col three">
        <div class="news-title"><span class="feed"></span>News &amp; Events</div>
        <div class="tabs"><span class="on">Latest News</span><span>Testimonials</span></div>
        <div class="news-item"><span class="headline">Lorem ipsum dolor sit amet, consectetuer</span>Ut wisi enim ad minim veniam, quis nostrud exerci tation ullamcorper suscipit lobortis nisl ut aliquip ex ea commodo consequat.</div>
        <div class="news-item"><span class="headline">Lorem ipsum dolor sit amet, consectetuer</span>Nam liber tempor cum soluta nobis eleifend option congue nihil imperdiet doming id quod mazim placerat facer possim assum.</div>
      </div>
    </section>
  </div>

  <footer class="footer">Copyright © 2011 Bright Shore <span>Catechetics</span>. All right reserved</footer>
</body>
</html>
```